Business Card Update, need to bring life to the card, two sided color

We need a new business card design, are moving and changing addresses and need a new look, we have the logos already attached but need a new style moving forward. Can incorporate the color of the logo (The Green) as well, maybe a solid back? We deal with safety products revolving around static electricity and safety lighting. Would like to keep same font in second logo as well.

Target Market(s)

Electrical Safety, Lighting

Contact Information for Business Card

Lars Whitcombe
Vice President
Office: 555-284-7316
Cell: 555-862-0457
lars@tkwhitcombe.com
www.tkwhitcombe.com
4700 West Cedar Boulevard
Suite #320
Roswell, GA 30412

Font styles to use
Serif
Sans Serif

Requirements
Must have
• Since 1918
Nice to have
• Could use the 100 Year Logo for back of card, would like the back of card to be the same green as logo.
Should not have
• No black cards please.

```html
<!DOCTYPE html>
<html lang="en">
<head>
<meta charset="utf-8">
<title>T.K. Whitcombe – Business Card</title>
<link rel="stylesheet" href="https://fonts.googleapis.com/css2?family=Open+Sans:wght@400;700&display=swap">
<style>
  :root {
    --backdrop: #2b2b2b;
    --brand-green: #1a9a57;
    --green-deep: #137a44;
    --card-white: #ffffff;
    --ink: #2a2a2a;
  }
  html, body {
    margin: 0;
    padding: 0;
    width: 1200px;
    height: 738px;
    overflow: hidden;
    background: var(--backdrop);
    font-family: "Open Sans", Arial, sans-serif;
  }
  .stage {
    position: relative;
    width: 1200px;
    height: 738px;
  }
  .card {
    position: absolute;
    top: 220px;
    width: 520px;
    height: 297px;
    box-sizing: border-box;
    box-shadow: 0 10px 30px rgba(0,0,0,0.45);
  }
  .card--back {
    left: 50px;
    background: var(--brand-green);
  }
  .card--front {
    left: 630px;
    background: var(--card-white);
  }
  .brand {
    position: absolute;
    left: 62px;
    top: 112px;
    display: flex;
    align-items: center;
    gap: 18px;
    color: var(--green-deep);
    font-weight: 700;
  }
  .brand__mark {
    width: 68px;
    height: 68px;
    border-radius: 50%;
    background: var(--green-deep);
    flex: none;
  }
  .brand__name {
    font-size: 28px;
    line-height: 1.05;
    letter-spacing: 0.5px;
  }
  .brand__sub {
    display: block;
    font-size: 14px;
    letter-spacing: 0.3px;
  }
  .since {
    position: absolute;
    right: 28px;
    bottom: 22px;
    margin: 0;
    color: var(--card-white);
    font-size: 13px;
    font-weight: 700;
    letter-spacing: 1.5px;
    text-transform: uppercase;
  }
  .contact {
    position: absolute;
    left: 38px;
    bottom: 26px;
    color: var(--ink);
    font-size: 13.5px;
    line-height: 1.3;
  }
  .contact__name {
    margin: 0;
    color: var(--brand-green);
    font-size: 18px;
    font-weight: 700;
    line-height: 1.2;
  }
  .contact__title {
    margin: 0 0 10px;
    font-size: 13.5px;
  }
  .contact__line { margin: 0; }
  .label, .accent { color: var(--brand-green); }
  .divider { color: var(--brand-green); font-weight: 700; padding: 0 4px; }
</style>
</head>
<body>
<main class="stage">
  <section class="card card--back" aria-label="Card back">
    <div class="brand">
      <span class="brand__mark" aria-hidden="true"></span>
      <span class="brand__name">T.K. Whitcombe
        <span class="brand__sub">Manufacturing Company, Inc.</span>
      </span>
    </div>
    <p class="since">Since 1918</p>
  </section>

  <section class="card card--front" aria-label="Card front">
    <div class="contact">
      <p class="contact__name">Lars Whitcombe</p>
      <p class="contact__title">Vice President</p>
      <p class="contact__line"><span class="label">Office:</span> 555-284-7316<span class="divider">|</span><span class="label">Cell:</span> 555-862-0457</p>
      <p class="contact__line">lars@tkwhitcombe.com<span class="divider">|</span>www.<span class="accent">tkwhitcombe</span>.com</p>
      <p class="contact__line">4700 West Cedar Boulevard, Suite #320</p>
      <p class="contact__line">Roswell, GA 30412</p>
    </div>
  </section>
</main>
</body>
</html>
```